Silver Ridge Harlow Basin Masters Week of Golf 2107

I would like a design for an A4 Event Flyer.

This is a golf event for Senior ladies and gentlemen. I would like the design to appeal to an older age group.

I would like somewhere on the flyer a golf ball image with the following details inside "Please put me on your notice board"

The information on the Flyer is as follows
- (Title - Silver ridge Harlow Basin Masters Week of Golf 2017)
- Date 16th of October to 20th of October
- Over 55 years of age
- We invite our fellow Veteran Ladies and Gentlemen to play a unique 54 hole stableford event at three fantastic Golf Courses, and finish the week at Penwick Golf club with a 2BBB Medley.
- Insert schedule that is attached in PDF. They layout can be changed.

- For entry form and details
Contact: Penwick Proshop on 02 69318842 or email admin@penwickdalbrookgolf.example.au

I have attached 4 golf course images. This is a photo of each course. Could I please get these added to the flyer.

Target Market(s)

seniors

Industry/Entity Type

Golf Course

Requirements
Must have
• All information provided

```html
<!DOCTYPE html>
<html lang="en">
<head>
<meta charset="utf-8">
<title>Silver Ridge Harlow Basin Masters – Week of Golf 2017</title>
<link href="https://fonts.googleapis.com/css2?family=Libre+Baskerville:wght@400;700&family=PT+Sans:ital,wght@0,400;0,700;1,700&display=swap" rel="stylesheet">
<style>
:root{
  --green-dark:#0f6b3a;
  --green-deep:#4e7d2f;
  --green-mid:#5e8f34;
  --green-light:#8cc63f;
  --green-bright:#7bbf3a;
  --text:#333;
  --white:#fff;
  --sky:#3d7fc4;
}
*{margin:0;padding:0;box-sizing:border-box}
html,body{width:866px;height:1200px;overflow:hidden;background:#fff}
.flyer{position:relative;width:866px;height:1200px;background:var(--white);font-family:"PT Sans",sans-serif;color:var(--text)}
.hero{position:absolute;left:0;top:0;width:866px;height:480px}
.hero-photo{position:absolute;inset:0;background:linear-gradient(160deg,#2f6fb8 0%,#6aa6dc 45%,#cfe0ee 70%,#b8c9d6 100%)}
.hero-wave{position:absolute;left:0;top:300px;width:866px;height:185px}
.notice-ball{position:absolute;left:35px;top:270px;width:192px;height:192px;border-radius:50%;
  background:radial-gradient(circle at 40% 35%,#fff 0%,#f3f3f3 55%,#d6d6d6 100%);
  box-shadow:0 4px 10px rgba(0,0,0,.35);display:flex;align-items:center;justify-content:center;text-align:center;
  font-style:italic;font-weight:700;color:var(--green-dark);font-size:21px;line-height:27px}
.title-block{position:absolute;left:0;width:866px;text-align:center;font-family:"Libre Baskerville",serif;color:var(--green-dark)}
.event-name{top:490px;font-size:28px;font-weight:700}
.rule{position:absolute;left:124px;width:606px;height:2px;background:var(--green-dark)}
.event-title{top:560px;font-size:40px;font-weight:700;letter-spacing:1px}
.event-dates{top:628px;font-size:26px}
.invite{position:absolute;left:60px;top:672px;width:746px;text-align:center;font-size:19px;line-height:24px}
.schedule{position:absolute;left:33px;top:746px;display:flex;gap:4px}
.day{width:130px;display:flex;flex-direction:column;gap:10px}
.day-name,.day-date,.day-info{box-shadow:0 2px 4px rgba(0,0,0,.25);color:var(--white);text-align:center}
.day-name{background:var(--green-mid);height:36px;font-size:14px;display:flex;flex-direction:column;justify-content:center;line-height:14px}
.day-name small{font-size:9px}
.day-date{background:var(--green-light);height:24px;font-size:12px;line-height:24px}
.day-info{background:var(--green-light);height:75px;padding-top:6px;font-size:10.5px;line-height:17px}
.day-info strong{display:block;font-size:12px}
.courses{position:absolute;top:920px;left:0;width:866px}
.course-photo{position:absolute;top:0;width:183px;height:116px;box-shadow:0 6px 6px -3px rgba(0,0,0,.35)}
.presentation{position:absolute;top:1073px;left:0;width:866px;text-align:center;font-family:"Libre Baskerville",serif;font-size:16px;color:var(--green-dark)}
.footer-wave{position:absolute;left:0;top:1098px;width:866px;height:102px}
.contact{position:absolute;top:1157px;left:0;width:866px;text-align:center;color:var(--white);font-size:20px}
</style>
</head>
<body>
<div class="flyer">
  <div class="hero">
    <div class="hero-photo" role="img" aria-label="Photo of a smiling senior couple holding golf clubs beneath palm trees and blue sky"></div>
    <svg class="hero-wave" viewBox="0 0 866 185" preserveAspectRatio="none">
      <path d="M0 120 C180 60 330 140 500 150 C650 160 780 120 866 60 L866 185 L0 185Z" fill="var(--green-bright)"/>
      <path d="M0 140 C180 90 330 165 500 175 C650 182 780 150 866 95 L866 185 L0 185Z" fill="var(--green-deep)"/>
      <path d="M0 150 C180 110 330 178 500 182 C650 186 780 165 866 120 L866 185 L0 185Z" fill="var(--white)"/>
    </svg>
    <div class="notice-ball">PLEASE<br>PUT ME ON YOUR<br>NOTICE BOARD</div>
  </div>

  <h1 class="title-block event-name">Silver ridge Harlow Basin Masters</h1>
  <div class="rule" style="top:544px"></div>
  <h2 class="title-block event-title">WEEK OF GOLF 2017</h2>
  <div class="rule" style="top:606px"></div>
  <p class="title-block event-dates">16th of October to 20th of October</p>

  <p class="invite">We invite our fellow Veteran Ladies and Gentlemen to play a unique 54 hole stableford event at three fantastic Golf Courses, and finish the week at Penwick Golf club with a 2BBB Medley.</p>

  <div class="schedule">
    <div class="day"><div class="day-name">SUNDAY</div><div class="day-date">15 October</div><div class="day-info"><strong>Penwick Golf Club</strong>Registrations:<br>4.00pm-6.00pm</div></div>
    <div class="day"><div class="day-name">MONDAY</div><div class="day-date">16 October</div><div class="day-info"><strong>Ashcombe Golf Course</strong>Par 72 Stableford -1st<br>Round Championships</div></div>
    <div class="day"><div class="day-name">TUESDAY<small>HBVGA Trophy Day</small></div><div class="day-date">17 October</div><div class="day-info"><strong>Marlow Golf Course</strong>Par 71 Stableford -2nd<br>Round Championships</div></div>
    <div class="day"><div class="day-name">WEDNESDAY</div><div class="day-date">18 October</div><div class="day-info"><strong>LEISURE</strong></div></div>
    <div class="day"><div class="day-name">THURSDAY</div><div class="day-date">19 October</div><div class="day-info"><strong>Briarwood Golf Course</strong>Par 72 Stableford -<br>Round 3 Championships</div></div>
    <div class="day"><div class="day-name">FRIDAY</div><div class="day-date">20 October</div><div class="day-info"><strong>Penwick Golf Course</strong>Par 66 18 Hole 2BBB<br>Medley Stableford</div></div>
  </div>

  <div class="courses">
    <div class="course-photo" style="left:40px;background:linear-gradient(160deg,#3f6b2a,#6f9a3e 60%,#4b7a2c)" role="img" aria-label="Golf course fairway with winding cart path"></div>
    <div class="course-photo" style="left:241px;background:linear-gradient(180deg,#4f8fd0 0%,#8cb8d8 35%,#6e8f3c 60%,#b0762e 100%)" role="img" aria-label="Golf course fairway under tree canopy"></div>
    <div class="course-photo" style="left:445px;background:linear-gradient(180deg,#6ea4d6 0%,#a9c8e0 40%,#5c8a35 60%,#79a845 100%)" role="img" aria-label="Golf course green with palm trees and a cart"></div>
    <div class="course-photo" style="left:644px;background:linear-gradient(180deg,#3e6f2a 0%,#79b043 50%,#8cc04f 80%,#e6dcc0 100%)" role="img" aria-label="Golf course green with bunker and flag"></div>
  </div>

  <p class="presentation">Penwick Golf Club ~ PRESENTATION DINNER DANCE ~ 7.00pm for 7.30pm</p>

  <svg class="footer-wave" viewBox="0 0 866 102" preserveAspectRatio="none">
    <path d="M0 95 C150 30 350 5 520 8 C680 10 790 30 866 45 L866 102 L0 102Z" fill="var(--green-bright)"/>
    <path d="M0 102 C160 45 360 25 530 28 C690 30 795 45 866 60 L866 102Z" fill="var(--green-deep)"/>
  </svg>
  <p class="contact">Penwick Proshop on <strong>02 69318842</strong> or email <strong>admin@penwickdalbrookgolf.example.au</strong></p>
</div>
</body>
</html>
```